Web Design Project for DJ

We need a web design for a DJ. Our client is a freelance DJ who already has a regular gig at a major night club but is looking to expand his exposure. He is located in a major metropolitan area and is looking for further gigs. He is hoping to generate further business via the website, including bookings via the site.

For reference his pagelinker page is here https://www.pagelinker.example/pages/DJ-Vorn/730162948415207

Following face to face discussions with the client today we have made a few small alterations to the brief.  We are hoping to have some images uploaded shortly.

Target Market(s)

Event planners, night club owners, radio stations, younger age groups (16-35)

Industry/Entity Type

Business

Requirements
Must have
• Name is DJVorn, this should obviously feature prominently. His current business card is attached as an example.

Links to Pagelinker and Tunedrift

Cool, modern look, slightly edgy.

Site will be built in Joomla, so a front page and secondary page template is required.
Nice to have
• Blog style layout to front page featuring recent and upcoming gigs.

Secondary pages may include a more expansive blog, a list of upcoming gigs, and a booking form.

Darker colour palettes preferred and use of same/similar fonts to those on the business card are an obvious plus

```html
<!DOCTYPE html>
<html lang="en">
<head>
<meta charset="utf-8">
<title>DJ Vorn</title>
<link href="https://fonts.googleapis.com/css2?family=Cabin:wght@400;600;700&display=swap" rel="stylesheet">
<style>
:root{
  --bg-deep:#050b3a;
  --bg-mid:#0b2a9a;
  --bg-glow:#1a5cff;
  --magenta:#ff2fd8;
  --magenta-soft:#e04ac8;
  --lime:#b8e83c;
  --violet:#9b3cff;
  --panel:rgba(10,24,90,.78);
  --white:#ffffff;
  --text:#e6ecff;
  --red:#ff2a2a;
  --grey-bar:#bfc4d0;
}
*{box-sizing:border-box;margin:0;padding:0}
html,body{width:933px;height:1200px;overflow:hidden}
body{
  position:relative;
  font-family:Arial,Helvetica,sans-serif;
  color:var(--text);
  background:
    radial-gradient(ellipse 70% 40% at 50% 95%,rgba(30,200,255,.35),transparent 70%),
    radial-gradient(ellipse 60% 50% at 50% 55%,var(--bg-glow),transparent 75%),
    linear-gradient(180deg,#000 0%,var(--bg-deep) 12%,var(--bg-mid) 55%,#0a3fb8 85%,#03103a 100%);
}
.spectrum-top{
  position:absolute;left:0;top:0;width:933px;height:110px;
  background:
    linear-gradient(180deg,rgba(0,0,0,0) 0%,rgba(5,11,58,.9) 100%),
    linear-gradient(90deg,#ff2a2a 0%,#ff3cd0 18%,#a040ff 34%,#2f7bff 48%,#1ee0ff 60%,#3cff6a 72%,#e8ff3a 84%,#ff9a2a 100%);
  opacity:.9;
}
.spectrum-bottom{
  position:absolute;left:0;bottom:0;width:933px;height:70px;
  background:
    linear-gradient(0deg,rgba(0,0,0,0) 40%,rgba(3,16,58,.9) 100%),
    linear-gradient(90deg,#ff3a3a 0%,#ffb82a 20%,#e8ff3a 38%,#3cff6a 55%,#1ee0ff 72%,#2f7bff 86%,#a040ff 100%);
  opacity:.8;
}
.brand{position:absolute;left:134px;top:40px}
.brand-name{
  font-family:'Cabin',sans-serif;font-weight:700;font-size:50px;letter-spacing:1px;color:#ff3030;line-height:1;
}
.main-nav{
  position:absolute;left:132px;top:111px;width:668px;height:39px;
  background:linear-gradient(180deg,#2a2a2a,#0a0a0a);
  border:1px solid var(--magenta);
  display:flex;align-items:center;justify-content:space-around;
  font-family:'Cabin',sans-serif;font-size:17px;font-weight:600;color:var(--magenta);
}
.panel{position:absolute;background:var(--panel)}
.content{left:132px;top:165px;width:438px;height:862px;border:2px solid var(--magenta-soft);box-shadow:0 0 8px var(--violet)}
.sidebar{left:586px;top:165px;width:214px;height:862px;border:2px solid var(--lime);box-shadow:0 0 8px var(--lime)}
.heading{
  position:absolute;font-family:'Cabin',sans-serif;font-weight:600;font-size:17px;color:var(--white);letter-spacing:.5px;white-space:nowrap;
}
.photo{position:absolute;border:2px solid #fff}
.player{
  position:absolute;left:8px;top:320px;width:418px;height:24px;background:#0c0c0c;border:1px solid #fff;
  display:flex;align-items:center;gap:8px;padding:0 8px;font-size:10px;color:#fff;font-weight:bold;
}
.player .track{flex:1;height:6px;background:#555}
.player .vol{width:52px;height:5px;background:#fff}
.copy{position:absolute;font-size:10.5px;line-height:1.3;color:var(--text)}
.share{position:absolute;display:flex;gap:12px;font-size:8px;color:#fff}
.share span{display:flex;align-items:center;gap:3px}
.share b{background:#dfe6f5;color:#223;font-weight:normal;padding:1px 4px}
.share i{display:inline-block;width:8px;height:8px;background:#3a5aa8}
.comment-tab{
  position:absolute;right:0;height:18px;width:96px;
  background:linear-gradient(180deg,#d6dae4,#a8aebd);
  clip-path:polygon(12px 0,100% 0,100% 100%,0 100%);
  font-size:10px;color:#222;display:flex;align-items:center;justify-content:flex-end;gap:6px;padding-right:6px;
}
.comment-tab b{background:#555;color:#fff;font-weight:normal;padding:0 4px}
.rule{position:absolute;left:0;width:434px;height:3px;background:var(--grey-bar)}
.date{position:absolute;font-size:10.5px;color:var(--red)}
.more{text-decoration:underline;color:#fff}
.search-box{
  position:absolute;left:15px;top:29px;width:173px;height:28px;background:#0a0a0a;border:1px solid #888;
  font-family:'Cabin',sans-serif;font-size:15px;color:#666;padding:4px 8px;
}
.social{position:absolute;left:15px;top:96px;width:180px;display:flex;flex-wrap:wrap;gap:4px}
.social span{font-family:'Cabin',sans-serif;font-size:10px;color:#fff;background:#1c2e86;padding:2px 5px;display:flex;align-items:center;gap:3px}
.social i{display:inline-block;width:7px;height:7px;background:var(--magenta)}
.caption{position:absolute;left:15px;width:175px;font-size:8.5px;line-height:1.25;color:var(--text)}
.meta{position:absolute;left:15px;width:160px;font-size:8.5px;color:#fff;display:flex;justify-content:space-between}
.meta u{color:#fff}
.footer{
  position:absolute;left:132px;top:1049px;width:668px;height:103px;
  background:rgba(4,14,60,.8);border:2px solid var(--lime);
}
.footer-col{position:absolute;top:6px}
.footer-col h3{font-family:'Cabin',sans-serif;font-weight:400;font-size:15px;color:var(--magenta);margin-bottom:2px}
.footer-col ul{list-style:none;font-size:9.5px;color:var(--magenta);line-height:14.4px;padding-left:6px;white-space:nowrap}
.footer-col .pair{display:flex;gap:8px}
</style>
</head>
<body>
<div class="spectrum-top" aria-hidden="true"></div>
<div class="spectrum-bottom" aria-hidden="true"></div>

<header class="brand">
  <span class="brand-name">DJ VORN</span>
</header>

<nav class="main-nav">
  <span>HOME</span><span>MUSIC</span><span>VIDEOS</span><span>PHOTOS</span><span>ALBUMS</span><span>ABOUT</span><span>CONTACT</span>
</nav>

<main class="panel content">
  <h1 class="heading" style="left:8px;top:4px">DJ VORN MAKE BASE FOR INSTRUMENT.</h1>
  <div class="photo" role="img" aria-label="Video still of the DJ at the decks in a club" style="left:1px;top:29px;width:434px;height:290px;background:linear-gradient(135deg,#5a3a2a,#2a1a1a 45%,#1a2a6a 80%,#3a4ab0)">
    <svg width="430" height="286" style="position:absolute;left:0;top:0" aria-hidden="true"><circle cx="214" cy="140" r="26" fill="rgba(255,255,255,.35)" stroke="rgba(255,255,255,.7)" stroke-width="3"/><polygon points="206,126 206,154 230,140" fill="rgba(255,255,255,.8)"/></svg>
  </div>
  <div class="player"><span>&#9654;</span><span>00:00</span><span class="track"></span><span>00:00</span><span>&#128264;</span><span class="vol"></span></div>
  <p class="copy" style="left:12px;top:356px;width:410px">Lorem Ipsum is simply dummy text of the printing and typesetting industry. Lorem Ipsum has been the industry's standard dummy text ever since the 1500s.</p>
  <div class="share" style="left:12px;top:398px"><span><i></i>Like <b>395</b></span><span><i></i>Post <b>83</b></span></div>
  <div class="comment-tab" style="top:405px">Comment. <b>13</b></div>
  <div class="rule" style="top:423px"></div>

  <h2 class="heading" style="left:8px;top:431px">LATEST BLOG POSTS.</h2>

  <div class="photo" role="img" aria-label="Blog photo of the DJ performing to a club crowd" style="left:6px;top:457px;width:250px;height:167px;background:linear-gradient(135deg,#2a3a7a,#101040 50%,#3a5ad0)"></div>
  <p class="date" style="left:260px;top:455px;width:160px;text-align:right">Posted On june / 20 / 13</p>
  <p class="copy" style="left:262px;top:472px;width:165px">Lorem Ipsum is simply dummy text of the printing and typesetting industry. Lorem Ipsum has been the industry's standard dummy text ever since the 1500s.<br><span class="more">See More</span></p>
  <div class="share" style="left:262px;top:597px"><span><i></i>Like <b>27</b></span><span><i></i>Post <b>9</b></span></div>
  <div class="comment-tab" style="top:619px">Comment. <b>7</b></div>
  <div class="rule" style="top:637px"></div>

  <div class="photo" role="img" aria-label="Blog photo of the DJ with a guest celebrating" style="left:6px;top:655px;width:250px;height:167px;background:linear-gradient(135deg,#7a1a2a,#3a1020 50%,#20204a)"></div>
  <p class="date" style="left:260px;top:653px;width:160px;text-align:right">Posted On June / 19 / 13</p>
  <p class="copy" style="left:262px;top:677px;width:165px">Lorem Ipsum is simply dummy text of the printing and typesetting industry. Lorem Ipsum has been the industry's standard dummy text ever since the 1500s.<br><span class="more">See More</span></p>
  <div class="share" style="left:262px;top:795px"><span><i></i>Like <b>28</b></span><span><i></i>Post <b>11</b></span></div>
  <div class="comment-tab" style="top:823px">Comment. <b>20</b></div>
  <div class="rule" style="top:841px"></div>
</main>

<aside class="panel sidebar">
  <h2 class="heading" style="left:15px;top:4px">Search.</h2>
  <div class="search-box">Here.</div>
  <h2 class="heading" style="left:15px;top:70px">SOCIAL MEDIA.</h2>
  <div class="social">
    <span><i></i>Pagelinker</span><span><i></i>Circlet</span><span><i></i>Chirpline</span><span><i></i>Tunedrift</span><span><i></i>Vidstream</span>
  </div>
  <h2 class="heading" style="left:15px;top:140px">TOP OF VIEW.</h2>
  <div class="photo" role="img" aria-label="Popular photo of the DJ at the mixer" style="left:15px;top:163px;width:157px;height:132px;background:linear-gradient(135deg,#1a2a5a,#0a1030 55%,#2a4ab0)"></div>
  <p class="caption" style="top:304px">Lorem Ipsum is simply dummy text of the printing and typesetting industry.</p>
  <p class="meta" style="top:327px"><u>View All</u><span>View Of 1,800</span></p>
  <div class="photo" role="img" aria-label="Popular photo of the DJ pointing to the crowd" style="left:15px;top:349px;width:157px;height:132px;background:linear-gradient(135deg,#6a3a3a,#2a1a1a 55%,#3a2a5a)"></div>
  <p class="caption" style="top:489px">Lorem Ipsum is simply dummy text of the printing and typesetting industry.</p>
  <p class="meta" style="top:512px"><u>View All</u><span>View Of 1,200</span></p>
  <h2 class="heading" style="left:15px;top:534px">RECENT POST.</h2>
  <div class="photo" role="img" aria-label="Recent photo of the DJ under green club lights" style="left:19px;top:557px;width:135px;height:116px;background:linear-gradient(135deg,#1ab04a,#0a3a2a 50%,#3a1aa0)"></div>
  <p class="caption" style="top:678px">Lorem Ipsum is text of the industry.<br><u>View All</u></p>
  <div class="photo" role="img" aria-label="Recent photo of the DJ under blue club lights" style="left:19px;top:703px;width:135px;height:116px;background:linear-gradient(135deg,#4a6aff,#1a2a8a 55%,#8a6ad0)"></div>
  <p class="caption" style="top:824px">Lorem Ipsum is text of the industry.<br><u>View All</u></p>
</aside>

<footer class="footer">
  <div class="footer-col" style="left:15px"><h3>Comin' Up</h3><ul><li>Makin' Noise</li><li>News</li><li>60 Seconds</li><li>Game Changer</li></ul></div>
  <div class="footer-col" style="left:158px"><h3>Music</h3><ul><li>Albums</li><li>Compilations</li><li>In The Bag</li><li>Reviews</li></ul></div>
  <div class="footer-col" style="left:294px"><h3>Related Post</h3><div class="pair"><ul><li>Albums</li><li>Compilations</li><li>In The Bag</li><li>Reviews</li></ul><ul><li>Albums</li><li>Compilations</li><li>In The Bag</li><li>Reviews</li></ul></div></div>
  <div class="footer-col" style="left:495px"><h3>Booking info</h3><ul><li>NAMe : Dj.Vorn</li><li>phone: (555) 014-2290</li><li>MANAGEMENT:&nbsp; Rowan Hale</li><li>E-Mail: Desk at Vorn 8</li><li>E-Mail: Tess at DJ Vorn 8</li></ul></div>
</footer>
</body>
</html>
```